Payroll Brochure

Create a brochure with the copy i have provided . A simple easy tp read brochure that shows wat we do we handle payroll taxes insurance 401k etc

```html
<!DOCTYPE html>
<html lang="en">
<head>
<meta charset="utf-8">
<title>Kestrel Payroll Brochure</title>
<link rel="stylesheet" href="https://fonts.googleapis.com/css2?family=Prata&family=Libre+Baskerville&display=swap">
<style>
:root{
  --bg:#ececec;
  --maroon-dark:#1f0f0c;
  --maroon:#4a1c14;
  --maroon-mid:#6a2a1c;
  --gold:#f2c23a;
  --gold-soft:#e0a93a;
  --brick:#8c1d14;
  --cream:#f1e6d6;
  --text:#dccfc0;
}
*{margin:0;padding:0;box-sizing:border-box}
html,body{width:1200px;height:2400px;overflow:hidden;background:var(--bg)}
body{position:relative;font-family:"Libre Baskerville",Georgia,serif;color:var(--text)}
.sheet{position:absolute;background:linear-gradient(180deg,var(--maroon-dark) 0%,var(--maroon) 45%,var(--maroon-mid) 75%,var(--maroon) 100%);overflow:hidden}
.panel{position:absolute;top:0;height:100%}
.abs{position:absolute}
.brand{position:absolute;font-family:"Prata",Georgia,serif;color:var(--brick);font-size:40px;letter-spacing:1px;display:flex;align-items:center;gap:10px}
.brand .dot{width:22px;height:22px;border-radius:50%;background:var(--brick)}
.center{left:0;right:0;text-align:center}
.title{font-family:"Prata",Georgia,serif;color:var(--gold);line-height:1}
.subtitle{font-family:"Prata",Georgia,serif;color:var(--cream)}
.rule{border-top:1px solid rgba(242,194,58,.5)}
.small{font-size:10px;color:var(--cream)}
.gold{color:var(--gold)}
.address{font-size:9px;color:var(--gold)}
.emblem{border-radius:50%;background:radial-gradient(circle,var(--gold) 0%,var(--gold-soft) 60%,rgba(224,169,58,0) 70%)}
.art{position:absolute;background:radial-gradient(ellipse at 50% 45%,#f6cf4a 0%,#c98a1e 45%,#2a140e 100%)}
.art-caption{position:absolute;left:0;right:0;bottom:0;background:var(--brick);color:var(--cream);font-family:"Prata",Georgia,serif;text-align:center}
.copy{position:absolute;font-size:6.6px;line-height:1.3;color:var(--text);text-align:justify}
.copy p{margin-bottom:5px}
.copy .lead{color:var(--gold)}
.sec-head{font-family:"Prata",Georgia,serif;color:var(--gold);font-size:13px;margin-bottom:6px;display:flex;align-items:center;gap:5px}
.sec-head svg{flex:none}
.phone{position:absolute;font-family:"Prata",Georgia,serif;color:var(--cream);font-size:28px}
</style>
</head>
<body>

<!-- Front cover panel -->
<section class="sheet" style="left:281px;top:115px;width:275px;height:581px">
  <div class="brand" style="left:70px;top:50px"><span class="dot"></span>Kestrel</div>
  <h1 class="title abs center" style="top:250px;font-size:36px">Payroll</h1>
  <p class="subtitle abs center" style="top:293px;font-size:15px">Taxes Insurance</p>
  <div class="rule abs" style="left:30px;right:30px;top:315px"></div>
  <p class="small abs center" style="top:322px">With Workers Compensation and Benefits</p>
  <div class="art" role="img" aria-label="Illustration of scattered gold coins" style="left:29px;top:381px;width:214px;height:111px">
    <div class="art-caption" style="font-size:13px;padding:3px 0">The Kestrel Advantage</div>
  </div>
  <p class="address abs center" style="top:544px">48 Birch Ave, 6th Floor, Alder Falls NY 12000</p>
</section>

<!-- Back cover panel -->
<section class="sheet" style="left:652px;top:115px;width:275px;height:581px">
  <div class="brand" style="left:68px;top:50px"><span class="dot"></span>Kestrel</div>
  <p class="subtitle abs center" style="top:210px;font-size:14px">Total</p>
  <h2 class="title abs center" style="top:224px;font-size:34px">Benefit</h2>
  <h2 class="title abs center" style="top:256px;font-size:26px">Management</h2>
  <div class="rule abs" style="left:30px;right:30px;top:288px"></div>
  <p class="address abs center" style="top:310px;font-size:10px">Contact-800-555-0142</p>
  <p class="address abs center" style="top:325px;font-size:10px">Place-48 Birch Ave, 6th Floor, Alder Falls NY 12000</p>
  <div class="emblem abs" style="left:115px;top:440px;width:90px;height:90px"></div>
</section>

<!-- Outside spread -->
<section class="sheet" style="left:173px;top:924px;width:887px;height:627px">
  <div class="panel" style="left:0;width:296px">
    <div class="copy" style="left:28px;top:100px;width:245px">
      <h3 class="sec-head" style="font-size:13px;line-height:1.2">What makes Kestrel uniquely qualified<br>to be your service provider?</h3>
      <p><span class="lead">People</span> Kestrel has gone to great lengths to hire and train a world-class team of experienced payroll and HR professionals who are genuinely interested in making sure our clients receive the very best in service and support.</p>
      <p><span class="lead">Process</span> Developed over the years, the Kestrel process has been designed with speed and accuracy in mind. We do what is needed to make sure our clients get speedy answers to their questions and produce accurate, reliable and timely payrolls. Our custom software is easily tailored to your payroll needs.</p>
      <p><span class="lead">Products</span> Kestrel has developed a comprehensive suite of products and services that will fit your needs.</p>
      <p><span class="lead">Flexibility</span> Kestrel will design HR solutions that meet your specific needs and requirements.</p>
    </div>
    <div class="copy" style="left:28px;top:300px;width:245px">
      <h3 class="sec-head" style="justify-content:center">Payroll</h3>
      <p><span class="lead">Flexible</span> – Our flexible and powerful payroll module allows you the ability to grow your business by meeting your unique needs.</p>
      <p><span class="lead">Efficient</span> – Get payroll done efficiently and accurately by relying on our flexible design to handle even the most complex payroll needs.</p>
      <p><span class="lead">Grow without Growing Pains</span> – Our technology and design are able to let you scale your business without adding all the incremental costs typically required.</p>
    </div>
    <div class="copy" style="left:28px;top:440px;width:245px">
      <h3 class="sec-head" style="justify-content:center">Tax Reporting &amp; Payments</h3>
      <p><span class="lead">Accurate</span> – all payroll taxes (federal, state, local) are calculated accurately. Additionally, we determine proper local tax jurisdictions based on the employee home and work addresses.</p>
      <p><span class="lead">Complete</span> – Federal, State and Local withholding taxes as well as State and Federal Unemployment taxes are provided. Tax payments are integrated into the Accounts Payable and General Ledger modules.</p>
    </div>
    <p class="phone" style="left:45px;top:570px">800-555-0142</p>
  </div>

  <div class="panel" style="left:296px;width:296px">
    <div class="brand" style="left:80px;top:55px"><span class="dot"></span>Kestrel</div>
    <p class="subtitle abs center" style="top:228px;font-size:15px">Total</p>
    <h2 class="title abs center" style="top:243px;font-size:36px">Benefit</h2>
    <h2 class="title abs center" style="top:278px;font-size:28px">Management</h2>
    <div class="rule abs" style="left:30px;right:30px;top:312px"></div>
    <p class="address abs center" style="top:333px;font-size:10px">Contact-800-555-0142</p>
    <p class="address abs center" style="top:349px;font-size:10px">Place-48 Birch Ave, 6th Floor, Alder Falls NY 12000</p>
    <div class="emblem abs" style="left:98px;top:470px;width:100px;height:100px"></div>
  </div>

  <div class="panel" style="left:592px;width:295px">
    <div class="brand" style="left:78px;top:55px"><span class="dot"></span>Kestrel</div>
    <h1 class="title abs center" style="top:272px;font-size:38px">Payroll</h1>
    <p class="subtitle abs center" style="top:314px;font-size:15px">Taxes, Insurance</p>
    <div class="rule abs" style="left:30px;right:30px;top:336px"></div>
    <p class="small abs center" style="top:344px">With Workers Compensation and Benefits</p>
    <div class="art" role="img" aria-label="Illustration of scattered gold coins" style="left:33px;top:416px;width:230px;height:113px">
      <div class="art-caption" style="font-size:14px;padding:3px 0">The Kestrel Advantage</div>
    </div>
    <p class="address abs center" style="top:584px">48 Birch Ave, 6th Floor, Alder Falls NY 12000</p>
  </div>
</section>

<!-- Inside spread -->
<section class="sheet" style="left:168px;top:1633px;width:885px;height:627px">
  <div class="panel" style="left:0;width:295px">
    <div class="copy" style="left:18px;top:92px;width:250px">
      <h3 class="sec-head"><svg width="9" height="7" viewBox="0 0 9 7"><path d="M0 3.5h7M4 0.5l3 3-3 3" stroke="#f1e6d6" fill="none"/></svg>Human Resources</h3>
      <p>With our online HR tools, you can empower yourself to take control of your human resource needs or let us do it.</p>
      <p><span class="lead">Get Big Company Services</span> – by using our online tools together with your service team, you have access to HR services only afforded by some of the largest companies.</p>
      <p><span class="lead">Library</span> – our online document library lets you and employees create your own library of information accessible at any time. Employees can upload documents and forms that can be kept in history as long as needed.</p>
    </div>
    <div class="copy" style="left:18px;top:220px;width:250px">
      <h3 class="sec-head"><svg width="9" height="7" viewBox="0 0 9 7"><path d="M0 3.5h7M4 0.5l3 3-3 3" stroke="#f1e6d6" fill="none"/></svg>Benefit Enrollment</h3>
      <p><span class="lead">Easy and Quick Enrollment</span> – our intuitive user experience quickly walks employees through their benefit enrollment process and allows them to compare plans and select those that best meet their needs.</p>
      <p><span class="lead">Flexible Benefit Plans and Easy Setup Options</span> – Offer your clients large-company benefit plans or administer their plans in an easy to use, yet flexible benefit administration module.</p>
      <p><span class="lead">You Pick</span> – with our flexible contribution setup features, you can contribute in any manner to your employees' benefits while the system automatically processes them through payroll.</p>
    </div>
    <div class="copy" style="left:18px;top:360px;width:250px">
      <h3 class="sec-head"><svg width="9" height="7" viewBox="0 0 9 7"><path d="M0 3.5h7M4 0.5l3 3-3 3" stroke="#f1e6d6" fill="none"/></svg>On Boarding</h3>
      <p><span class="lead">Customize your On Boarding</span> – you can customize your on boarding experience to your hiring needs as well as provide multiple workflows for different employee types. The on boarding experience can be branded for you, providing a personalized experience for the employees.</p>
      <p><span class="lead">Custom Document Management</span> – our custom document mapping feature lets you use your own forms and documents as part of the on boarding and hiring process. When these forms are completed they are electronically signed and stay in history as long as needed.</p>
      <p><span class="lead">Intuitive</span> – with a focus on the user experience, your employees will find it easy and quick to get on boarded with you.</p>
    </div>
    <div class="art" role="img" aria-label="Illustration of stacked gold coins" style="left:28px;top:510px;width:240px;height:117px;background:linear-gradient(180deg,rgba(0,0,0,0) 0%,#c98a1e 70%,#f2c23a 100%)"></div>
  </div>

  <div class="panel" style="left:295px;width:295px">
    <div class="copy" style="left:18px;top:140px;width:258px">
      <h3 class="sec-head"><svg width="9" height="7" viewBox="0 0 9 7"><path d="M0 3.5h7M4 0.5l3 3-3 3" stroke="#f1e6d6" fill="none"/></svg>Applicant Tracking</h3>
      <p><span class="lead">Create and Post Jobs</span> – you can create jobs with just a few clicks and post them on all the popular job sites.</p>
      <p><span class="lead">Hire the Right People</span> – by posting on popular job boards, as well as a proprietary database of job seekers, you will reach more candidates. You can choose to receive profiles of candidates that only match your background and specifications.</p>
      <p><span class="lead">Manage the Hiring Process</span> – review candidates via video or online conferencing, review voice interviews, schedule in person interviews, have candidates answer certain online questions, and manage this entire process to find the right people. Once hired, they can be on boarded automatically.</p>
    </div>
    <div class="copy" style="left:18px;top:270px;width:258px">
      <h3 class="sec-head"><svg width="9" height="7" viewBox="0 0 9 7"><path d="M0 3.5h7M4 0.5l3 3-3 3" stroke="#f1e6d6" fill="none"/></svg>Time and Attendance</h3>
      <p><span class="lead">Make Time Entry Easy</span> – Simplify time tracking so you can spend less time on payroll tasks.</p>
      <p><span class="lead">Everywhere Access</span> – Web interface, mobile apps, and on-premise time clocks allow employees to log their time wherever they are.</p>
      <p><span class="lead">Plug and Play Time Clocks</span> – Time clocks are delivered ready-to-use with little or no setup required.</p>
    </div>
    <div class="copy" style="left:18px;top:372px;width:258px">
      <h3 class="sec-head"><svg width="9" height="7" viewBox="0 0 9 7"><path d="M0 3.5h7M4 0.5l3 3-3 3" stroke="#f1e6d6" fill="none"/></svg>ACA Compliance</h3>
      <p><span class="lead">Client Tools</span> – provide you with reporting and analysis tools online so you can monitor ACA information and be proactive in managing your needs.</p>
      <p><span class="lead">Affordability Test</span> – provide you with information about plan affordability with their employees so they can stay in compliance.</p>
      <p><span class="lead">Large Employer Analysis</span> – analyze your control groups to determine if you will fall under the rules of ACA for large employer groups.</p>
    </div>
    <div class="brand" style="left:80px;top:522px"><span class="dot"></span>Kestrel</div>
    <p class="small abs center" style="top:598px;font-size:9px">48 Birch Ave, 6th Floor, Alder Falls NY 12000</p>
  </div>

  <div class="panel" style="left:590px;width:295px">
    <div class="art" role="img" aria-label="Illustration of falling gold coins" style="left:8px;top:33px;width:280px;height:160px;background:radial-gradient(ellipse at 50% 50%,#f6cf4a 0%,#c98a1e 45%,rgba(42,20,14,0) 75%)"></div>
    <div class="copy" style="left:18px;top:248px;width:258px">
      <h3 class="sec-head"><svg width="9" height="7" viewBox="0 0 9 7"><path d="M0 3.5h7M4 0.5l3 3-3 3" stroke="#f1e6d6" fill="none"/></svg>Self Service</h3>
      <p><span class="lead">Managers</span> – your managers have access to their information via a highly intuitive online portal. Users can enter payroll time, create ad-hoc reports, preview and approve payroll and invoices, get invoice and check history, access employee records, communicate with employees, create, etc. One single sign on allows managers that may have multiple business entities to use one login.</p>
      <p><span class="lead">Employees</span> – employees can access pay information, request PTO, enroll in benefits, communicate with other employees, and access or change their personal information. They can also access company documents for review and upload personal documents as well.</p>
    </div>
    <div class="copy" style="left:18px;top:376px;width:258px">
      <h3 class="sec-head"><svg width="9" height="7" viewBox="0 0 9 7"><path d="M0 3.5h7M4 0.5l3 3-3 3" stroke="#f1e6d6" fill="none"/></svg>WOTC</h3>
      <p><span class="lead">Big Credits</span> – Work Opportunity Tax Credits (WOTC) allow you to receive between $2,400 and $9,600 for hiring eligible employees.</p>
      <p><span class="lead">Easy and Quick</span> – Employees complete a simple questionnaire to determine eligibility for WOTC. All of the necessary filing and reporting is handled for you and your client.</p>
      <p><span class="lead">Integrated</span> – WOTC is integrated wherever you would enter a new employee: back office payroll, online on boarding, and applicant tracking to ensure all employees are being evaluated.</p>
    </div>
    <div class="copy" style="left:18px;top:490px;width:258px">
      <h3 class="sec-head"><svg width="9" height="7" viewBox="0 0 9 7"><path d="M0 3.5h7M4 0.5l3 3-3 3" stroke="#f1e6d6" fill="none"/></svg>Workers Compensation and Benefits</h3>
      <p style="margin-bottom:1px">Pay as you go Workers' Compensation – Multiple carriers available</p>
      <p style="margin-bottom:1px">Access to a Multiple Employer 401K</p>
      <p>Access to various voluntary benefits</p>
    </div>
    <p class="phone" style="left:45px;top:572px">800-555-0142</p>
  </div>
</section>

</body>
</html>
```